Natural Food Packaging - Peanut Butter bars

Name, branding, trade dress for new line of natural/organic peanut based protein bars. The concept its to package a high value natural product for mass consumer consumption.

There will be 2 to 4 flavors initially introduced. Each flavor has a printed film wrapper and shelf display box. The design winner will have first preference for all the packaging work.Think peanut butter chocolate chip, peanut butter with cranberries, coconut, etc.

We are a privately owned, internationally established organic food manufacturer.

This will be a high profile, well recognized project within the industry.

It is an excellent opportunity for a long term business relationship.

Brisco Market(s)

consumers who want a better quality protein bar than they currently buy. Mostly active adults age 18-50

Industry/Entity Type

Business

Requirements
Must have
• A product name/brand and general look and feel. It needs to convey purity, great ingredients/quality, taste and great price.

It needs to have mass appeal...think Brisco and Zipo, not just Verdano Market.
Nice to have
• Package mock up images for 2 or 3 flavors

```html
<!DOCTYPE html>
<html lang="en">
<head>
<meta charset="utf-8">
<title>Marlow naturals – peanut protein bar packaging</title>
<link rel="stylesheet" href="https://fonts.googleapis.com/css2?family=Amatic+SC:wght@400;700&family=Architects+Daughter&display=swap">
<style>
  :root {
    --page: #ffffff;
    --kraft: #d2a878;
    --kraft-light: #dcb88c;
    --ink: #2b2220;
    --panel: #2d2523;
    --paper-line: #f3e6d3;
    --strawberry: #b8161c;
    --apple: #4e8a1f;
    --chocolate: #5b3216;
    --banana: #d7a219;
    --berry: #8a1f48;
    --wood-light: #c9a47a;
    --wood-dark: #6e4a2c;
  }
  * { box-sizing: border-box; margin: 0; padding: 0; }
  html, body { width: 1200px; height: 900px; overflow: hidden; background: var(--page); }
  .canvas { position: relative; width: 1200px; height: 900px; }

  /* bar wrapper */
  .wrapper {
    position: absolute; left: 78px; width: 514px; height: 130px;
    display: flex;
    background: linear-gradient(180deg, var(--kraft-light), var(--kraft));
    font-family: "Architects Daughter", cursive;
  }
  .wrapper--strawberry { top: 106px; --flavor: var(--strawberry); }
  .wrapper--apple      { top: 248px; --flavor: var(--apple); }
  .wrapper--chocolate  { top: 390px; --flavor: var(--chocolate); }
  .wrapper--banana     { top: 532px; --flavor: var(--banana); }
  .wrapper--berry      { top: 675px; --flavor: var(--berry); }

  .claim-band {
    width: 100px; height: 100%; background: var(--flavor);
    padding: 4px 6px 0 8px;
    font-family: "Amatic SC", sans-serif; font-weight: 700;
    color: var(--paper-line); line-height: 1;
  }
  .claim-band span { display: block; border-bottom: 1px dashed rgba(255,255,255,.55); padding-bottom: 1px; }
  .claim-band .claim-lg { font-size: 26px; }
  .claim-band .claim-sm { font-size: 18px; }

  .label-body { position: relative; flex: 1; }
  .tagline {
    position: absolute; left: 12px; top: 9px; font-size: 10px; color: var(--flavor);
    border-bottom: 1px dashed var(--ink); padding-bottom: 3px; width: 182px;
  }
  .benefits {
    position: absolute; left: 222px; top: 8px; font-size: 9px; line-height: 1.25;
    color: #fff; text-align: right;
  }
  .brand-name {
    position: absolute; left: 26px; top: 34px;
    font-size: 58px; line-height: 1; color: var(--ink);
  }
  .brand-sub {
    position: absolute; left: 152px; top: 92px;
    font-size: 15px; letter-spacing: 3px; color: var(--ink);
  }
  .weight {
    position: absolute; left: 258px; top: 98px; width: 20px; height: 20px; border-radius: 50%;
    border: 1px solid #fff; color: #fff; font-size: 7px; text-align: center; line-height: 18px;
  }

  .flavor-band {
    width: 34px; height: 100%; background: var(--flavor);
    writing-mode: vertical-rl; text-align: center;
    font-family: "Amatic SC", sans-serif; font-weight: 700; font-size: 17px;
    color: var(--paper-line); line-height: 34px; white-space: nowrap;
  }
  .ingredient-panel {
    width: 95px; height: 100%; background: var(--panel); position: relative;
  }
  .ingredient-panel::before, .ingredient-panel::after {
    content: ""; position: absolute; left: 10px; right: 10px; border-top: 1px dashed rgba(255,255,255,.6);
  }
  .ingredient-panel::before { top: 10px; }
  .ingredient-panel::after { bottom: 10px; }
  .ingredient-sketch {
    position: absolute; left: 18px; top: 18px; width: 60px; height: 94px;
    background: radial-gradient(circle, #4a403c 0%, var(--panel) 75%);
    border-radius: 6px;
  }

  /* display box header card */
  .display-header {
    position: absolute; left: 633px; top: 75px; width: 527px; height: 160px;
  }
  .wood-grain {
    position: absolute; inset: 0;
    background: linear-gradient(90deg, var(--wood-dark) 0%, var(--wood-light) 18%, #a57a52 40%, var(--wood-light) 62%, #8c6240 82%, var(--wood-light) 100%);
  }
  .header-panel {
    position: absolute; left: 40px; top: 42px; width: 390px; height: 102px; background: var(--panel);
    font-family: "Architects Daughter", cursive; color: #fff;
  }
  .header-panel .brand-name { color: #fff; left: 36px; top: 10px; font-size: 68px; }
  .header-panel .brand-sub { color: #fff; left: 210px; top: 74px; font-size: 16px; }
  .fruit-sketch {
    position: absolute; left: 440px; top: 58px; width: 60px; height: 70px;
    background: radial-gradient(circle, #e8dccd 0%, transparent 70%);
  }
  .flavor-ribbon {
    position: absolute; left: 338px; top: 6px; width: 180px; height: 30px;
    background: var(--strawberry); transform: rotate(8deg);
    font-family: "Amatic SC", sans-serif; font-weight: 700; font-size: 20px; color: var(--paper-line);
    text-align: center; line-height: 30px;
  }
</style>
</head>
<body>
<main class="canvas">

  <section class="wrapper wrapper--strawberry">
    <div class="claim-band"><span class="claim-lg">PROTEIN</span><span class="claim-sm">POWER SNACK</span><span class="claim-sm">NATURAL</span><span class="claim-lg">PEANUT</span><span class="claim-lg">FLAVOR</span></div>
    <div class="label-body">
      <p class="tagline">premium peanut based protein bar</p>
      <p class="benefits">100% natural<br>low fat<br>high energie</p>
      <p class="brand-name">Marlow</p>
      <p class="brand-sub">naturals</p>
      <p class="weight">40g</p>
    </div>
    <div class="flavor-band">PEANUT&amp;STRAWBERRY</div>
    <div class="ingredient-panel"><div class="ingredient-sketch" role="img" aria-label="Chalk sketch of a peanut and a strawberry"></div></div>
  </section>

  <section class="wrapper wrapper--apple">
    <div class="claim-band"><span class="claim-lg">PROTEIN</span><span class="claim-sm">POWER SNACK</span><span class="claim-sm">NATURAL</span><span class="claim-lg">PEANUT</span><span class="claim-lg">FLAVOR</span></div>
    <div class="label-body">
      <p class="tagline">premium peanut based protein bar</p>
      <p class="benefits">100% natural<br>low fat<br>high energie</p>
      <p class="brand-name">Marlow</p>
      <p class="brand-sub">naturals</p>
      <p class="weight">40g</p>
    </div>
    <div class="flavor-band">PEANUT&amp;APPLE</div>
    <div class="ingredient-panel"><div class="ingredient-sketch" role="img" aria-label="Chalk sketch of a peanut and an apple"></div></div>
  </section>

  <section class="wrapper wrapper--chocolate">
    <div class="claim-band"><span class="claim-lg">PROTEIN</span><span class="claim-sm">POWER SNACK</span><span class="claim-sm">NATURAL</span><span class="claim-lg">PEANUT</span><span class="claim-lg">FLAVOR</span></div>
    <div class="label-body">
      <p class="tagline">premium peanut based protein bar</p>
      <p class="benefits">100% natural<br>low fat<br>high energie</p>
      <p class="brand-name">Marlow</p>
      <p class="brand-sub">naturals</p>
      <p class="weight">40g</p>
    </div>
    <div class="flavor-band">PEANUT&amp;CHOCOLATE</div>
    <div class="ingredient-panel"><div class="ingredient-sketch" role="img" aria-label="Chalk sketch of a peanut and a chocolate bar"></div></div>
  </section>

  <section class="wrapper wrapper--banana">
    <div class="claim-band"><span class="claim-lg">PROTEIN</span><span class="claim-sm">POWER SNACK</span><span class="claim-sm">NATURAL</span><span class="claim-lg">PEANUT</span><span class="claim-lg">FLAVOR</span></div>
    <div class="label-body">
      <p class="tagline">premium peanut based protein bar</p>
      <p class="benefits">100% natural<br>low fat<br>high energie</p>
      <p class="brand-name">Marlow</p>
      <p class="brand-sub">naturals</p>
      <p class="weight">40g</p>
    </div>
    <div class="flavor-band">PEANUT&amp;BANANA</div>
    <div class="ingredient-panel"><div class="ingredient-sketch" role="img" aria-label="Chalk sketch of a peanut and a banana"></div></div>
  </section>

  <section class="wrapper wrapper--berry">
    <div class="claim-band"><span class="claim-lg">PROTEIN</span><span class="claim-sm">POWER SNACK</span><span class="claim-sm">NATURAL</span><span class="claim-lg">PEANUT</span><span class="claim-lg">FLAVOR</span></div>
    <div class="label-body">
      <p class="tagline">premium peanut based protein bar</p>
      <p class="benefits">100% natural<br>low fat<br>high energie</p>
      <p class="brand-name">Marlow</p>
      <p class="brand-sub">naturals</p>
      <p class="weight">40g</p>
    </div>
    <div class="flavor-band">PEANUT&amp;BANANA</div>
    <div class="ingredient-panel"><div class="ingredient-sketch" role="img" aria-label="Chalk sketch of a peanut and a jam jar"></div></div>
  </section>

  <section class="display-header">
    <div class="wood-grain" role="img" aria-label="Weathered wood plank texture"></div>
    <div class="header-panel">
      <p class="brand-name">Marlow</p>
      <p class="brand-sub">naturals</p>
    </div>
    <div class="fruit-sketch" role="img" aria-label="Chalk sketch of a strawberry"></div>
    <div class="flavor-ribbon">PEANUT&amp;STRAWBERRY</div>
  </section>

</main>
</body>
</html>
```